make a fireworks website

we are manufacturer of fireworks in Asia.
we need a HD fireworks website for showing product to all world customers.
we also need an register for member system,location, forum,products..etc
I added my Logo for the company.
brightpeonyhall.com.hk

and please message me if you have
any question.
here some example of website:
http://www.lanternmoth.com/
http://www.korvelmist.com/
http://www.tindle-orbwick.co.uk/
http://www.pemberlyspark.co.uk/

```html
<!DOCTYPE html>
<html lang="en">
<head>
<meta charset="utf-8">
<title>Bright Peony Hall – Fireworks &amp; FX</title>
<link href="https://fonts.googleapis.com/css2?family=Open+Sans:ital,wght@0,400;0,600;0,700;1,700;1,800&display=swap" rel="stylesheet">
<style>
:root{
  --pink:#ec1b6f;
  --pink-dark:#c8125b;
  --ink:#222;
  --text:#555;
  --muted:#888;
  --line:#e4e4e4;
  --night:#0d0b1a;
  --footer:#1c1c1c;
  --footer-deep:#111;
  --yellow:#fff3b0;
}
*{box-sizing:border-box;margin:0;padding:0}
html,body{width:1200px;height:2416px;overflow:hidden}
body{font-family:"Open Sans",Arial,sans-serif;color:var(--text);background:#fff;font-size:12px;line-height:1.55}
.wrap{width:1000px;margin:0 auto;position:relative}
a{color:inherit;text-decoration:none}

/* header */
.site-header{height:86px}
.site-header .wrap{display:flex;justify-content:space-between;align-items:center;height:86px}
.brand{display:flex;align-items:center;gap:10px}
.brand-dot{width:40px;height:40px;border-radius:50%;background:var(--pink)}
.brand-name{font-size:24px;font-weight:700;color:var(--pink);letter-spacing:-.3px}
.nav{text-align:right}
.nav-top{display:flex;gap:16px;justify-content:flex-end;font-size:10px;font-weight:600;color:var(--ink);letter-spacing:.5px}
.nav-main{display:flex;gap:26px;justify-content:flex-end;margin-top:8px;font-size:14px;font-weight:700;color:var(--ink)}
.nav-main span.caret{font-size:9px;margin-left:3px}

/* pink bar */
.topbar{height:22px;background:var(--pink);color:#fff;font-size:9px;font-weight:600}
.topbar .wrap{display:flex;align-items:center;height:22px;gap:8px}
.soc{width:11px;height:11px;border-radius:50%;background:#fff;opacity:.9;display:inline-block}
.topbar .phone{margin-left:18px}
.topbar .search{margin-left:auto;width:150px;height:15px;background:#fff;border-radius:2px}

/* hero */
.hero{height:300px;position:relative;background:radial-gradient(ellipse at 70% 45%,#c23a6a 0%,#5d1f4e 22%,#1a1233 48%,var(--night) 75%)}
.hero-art{position:absolute;inset:0}
.hero .wrap{padding-top:90px}
.hero .eyebrow{color:#fff;font-size:15px;font-weight:600;letter-spacing:1px}
.hero h1{color:#fff;font-size:38px;font-weight:800;line-height:1.05;letter-spacing:.5px}
.hero p{color:#ddd;font-size:10px;margin-top:8px;width:230px}
.btn{display:inline-block;background:var(--pink);color:#fff;font-size:10px;font-weight:700;padding:7px 16px;letter-spacing:.5px}
.hero .btn{margin-top:14px}

/* events strip */
.events{height:190px;position:relative;background:linear-gradient(90deg,#fff 0%,#fff 38%,#f6e6ef 48%,#2a1030 60%,#6a1f4c 80%,#f0a020 100%)}
.events-art{position:absolute;left:520px;right:0;top:0;bottom:0;background:radial-gradient(circle at 40% 50%,#f3c44b 0%,#d8456e 25%,#3b1340 55%,rgba(20,10,30,.2) 100%)}
.events-banner{position:absolute;left:100px;top:50px;background:var(--pink);color:#fff;padding:12px 22px 10px;width:330px}
.events-banner h2{font-size:19px;font-style:italic;font-weight:800;letter-spacing:.3px}
.events-banner p{font-size:9px;color:#ffe0ee}

/* fx */
.fx{height:402px;text-align:center}
.fx h2,.section-title{color:var(--pink);font-style:italic;font-weight:800;font-size:30px}
.fx h2{padding-top:14px}
.fx .lead{width:620px;margin:8px auto 0;font-size:10px;color:var(--muted)}
.fx .actions{margin-top:12px;display:flex;gap:8px;justify-content:center}
.products{display:flex;gap:30px;justify-content:center;margin-top:22px}
.product{width:190px;text-align:left}
.product .thumb{height:130px;border:1px solid var(--line);display:flex;align-items:center;justify-content:center}
.product .thumb div{width:110px;height:100px;border-radius:4px}
.product h3{font-size:11px;color:var(--ink);margin-top:8px;font-weight:700}
.product .rrp{font-size:9px;color:var(--muted)}
.product .price{font-size:13px;color:var(--ink);font-weight:700}
.product .price b{color:var(--pink)}
.product .buy{float:right;background:var(--pink);color:#fff;font-size:8px;padding:3px 7px;margin-top:2px}
.dots{display:flex;gap:6px;justify-content:center;margin-top:20px}
.dots i{width:8px;height:8px;border-radius:50%;background:#ccc}
.dots i.on{background:var(--pink)}

/* display */
.display{height:270px;background:var(--pink);position:relative}
.display-art{position:absolute;left:130px;top:10px;width:300px;height:260px;background:linear-gradient(180deg,#f7d34a 0%,#4fb7e8 35%,#8ad049 60%,#f06aa5 100%);opacity:.9;border-radius:4px 4px 0 0}
.display-copy{position:absolute;left:620px;top:26px;width:400px;color:#fff}
.display-copy h2{font-size:16px;font-style:italic;font-weight:800}
.display-copy p{font-size:9px;color:#ffe4ef;margin-top:6px}
.tabs{display:flex;gap:6px;margin-top:16px}
.tabs span{border:1px solid #fff;font-size:8px;padding:4px 12px;color:#fff}
.tabs span.on{background:var(--footer);border-color:var(--footer)}

/* content */
.content{height:590px}
.content .wrap{display:flex;gap:40px;padding-top:26px}
.article{width:660px}
.article h2{color:var(--pink);font-size:18px;font-weight:600;margin:0 0 6px}
.article p{font-size:10px;color:var(--muted);margin-bottom:10px}
.article section{margin-bottom:12px}
.aside{width:300px;padding-top:50px}
.quote{background:var(--yellow);padding:14px;font-size:10px;font-style:italic;color:#555}
.quote b{display:block;font-style:normal;margin-top:8px;color:var(--ink)}
.promo{background:var(--pink);color:#fff;padding:14px;margin-top:14px;font-size:10px;height:110px}
.promo b{font-size:13px}
.brochure{margin-top:16px;display:flex;align-items:center;gap:10px}
.brochure .ico{width:30px;height:36px;background:var(--pink)}
.brochure small{display:block;font-size:8px;color:var(--muted)}
.brochure strong{font-size:17px;font-style:italic;color:var(--pink);font-weight:800}

/* testimonials */
.testimonials{height:200px;text-align:center}
.testimonials .section-title{padding-top:10px}
.testimonials blockquote{position:relative;width:760px;margin:14px auto 0;font-size:10px;color:var(--muted);text-align:left}
.testimonials blockquote::before{content:"\201C";position:absolute;left:-40px;top:-20px;font-size:60px;color:var(--ink);font-weight:700}
.testimonials .dots{margin-top:16px}

/* footer */
.site-footer{height:310px;background:var(--footer);color:#bbb}
.site-footer .wrap{display:flex;gap:60px;padding-top:28px}
.site-footer h4{color:#fff;font-size:11px;letter-spacing:1px;margin-bottom:12px}
.links ul{list-style:none;columns:2;column-gap:60px;font-size:10px;line-height:2}
.follow li{list-style:none;display:flex;align-items:center;gap:8px;font-size:10px;margin-bottom:8px}
.follow .soc{width:18px;height:18px;background:#fff}
.offers p{font-size:9px}
.offers .field{height:22px;background:#fff;margin-top:10px;width:260px}
.offers .btn{margin-top:8px}
.pay{font-size:9px;margin-top:22px}
.pay b{color:#fff}
.cards{display:flex;gap:6px;margin-top:8px}
.cards i{width:36px;height:22px;background:#4a4a4a;border-radius:2px}
.legal{height:46px;background:var(--footer-deep);color:#888;font-size:9px}
.legal .wrap{display:flex;justify-content:space-between;align-items:center;height:46px}
</style>
</head>
<body>

<header class="site-header">
  <div class="wrap">
    <a class="brand" href="#"><span class="brand-dot"></span><span class="brand-name">Bright Peony Hall</span></a>
    <nav class="nav">
      <div class="nav-top"><span>ABOUT</span><span>SHOP</span><span>GALLERY</span><span>SAFETY</span><span>DELIVERY</span><span>BLOG</span><span>FAQS</span><span>CART</span></div>
      <div class="nav-main"><span>PRODUCTS<span class="caret">▼</span></span><span>EVENT DISPLAYS<span class="caret">▼</span></span><span>CONTACT US</span></div>
    </nav>
  </div>
</header>

<div class="topbar">
  <div class="wrap">
    <span>FOLLOW US ON:</span><i class="soc"></i><i class="soc"></i><i class="soc"></i>
    <span class="phone">☎ 0800 212 4477</span>
    <span class="search"></span>
  </div>
</div>

<section class="hero">
  <div class="hero-art" role="img" aria-label="Night sky filled with bursting pink, red and gold fireworks"></div>
  <div class="wrap">
    <div class="eyebrow">PERFECT FOR YOUR</div>
    <h1>SPECIAL DAY</h1>
    <p>Light up weddings, birthdays and parties with our full range of shells.</p>
    <a class="btn" href="#">SHOP NOW</a>
  </div>
</section>

<section class="events">
  <div class="events-art" role="img" aria-label="Golden and pink firework bursts over a dark sky"></div>
  <div class="events-banner">
    <h2>MEMORABLE EVENTS MADE EASY</h2>
    <p>Let our display experts plan the whole show</p>
  </div>
</section>

<section class="fx">
  <h2>Fireworks &amp; FX</h2>
  <p class="lead">We design and manufacture cakes, rockets, fountains and stage effects for customers all over the world. Every item is tested for colour, height and safety before it leaves our factory, so your show looks as bright as it should and runs without a hitch.</p>
  <div class="actions"><a class="btn" href="#">SHOP FIREWORKS</a><a class="btn" href="#">CUSTOMER ZONE</a></div>
  <div class="products">
    <article class="product"><div class="thumb"><div role="img" aria-label="Boxed firework cake" style="background:linear-gradient(135deg,#3b6fd1,#e84a8a)"></div></div><h3>Thunderbolt</h3><div class="rrp">RRP $59.99</div><div class="price">Our Price <b>$44.99</b><span class="buy">BUY</span></div></article>
    <article class="product"><div class="thumb"><div role="img" aria-label="Boxed firework cake" style="background:linear-gradient(135deg,#f4b632,#d3322f)"></div></div><h3>Magical Stars</h3><div class="rrp">RRP $59.99</div><div class="price">Our Price <b>$44.99</b><span class="buy">BUY</span></div></article>
    <article class="product"><div class="thumb"><div role="img" aria-label="Boxed firework cake" style="background:linear-gradient(135deg,#8a2bb8,#f06a2b)"></div></div><h3>Golden Rain</h3><div class="rrp">RRP $59.99</div><div class="price">Our Price <b>$44.99</b><span class="buy">BUY</span></div></article>
    <article class="product"><div class="thumb"><div role="img" aria-label="Boxed firework cake" style="background:linear-gradient(135deg,#1d2a6b,#3fa9e0)"></div></div><h3>Blue Storm</h3><div class="rrp">RRP $59.99</div><div class="price">Our Price <b>$44.99</b><span class="buy">BUY</span></div></article>
  </div>
  <div class="dots"><i class="on"></i><i></i><i></i></div>
</section>

<section class="display">
  <div class="display-art" role="img" aria-label="Row of colourful striped firework rockets"></div>
  <div class="display-copy">
    <h2>Professional Firework Display &amp; Events</h2>
    <p>Our licensed team stages full displays for festivals, city celebrations, corporate launches and private parties. We handle design, permits, setup and firing, so you can simply enjoy the night with your guests.</p>
    <p>Choose a package below or talk to us about a show built around your music, venue and budget.</p>
    <div class="tabs"><span class="on">WEDDINGS</span><span>CORPORATE</span><span>FESTIVALS</span><span>PARTIES</span></div>
  </div>
</section>

<section class="content">
  <div class="wrap">
    <div class="article">
      <section><h2>Fireworks for Sale Online</h2>
        <p>Order direct from the factory and save. Our online shop lists every product with video, effect time and shot count, so you know exactly what you are buying before it ships to your door.</p>
        <p>Wholesale buyers can register for a member account to see trade prices, track orders and download product sheets.</p></section>
      <section><h2>Professionally Organised New Years Eve Fireworks Event</h2>
        <p>Ring in the new year with a show timed to the second. We plan the layout, supply the product and fire everything from a safe distance using electronic systems.</p>
        <p>Tell us your venue and crowd size and we will send a full proposal within two working days.</p></section>
      <section><h2>The Perfect Addition to Any Event</h2>
        <p>From a short burst at a wedding to a long finale at a sports final, fireworks give any event a moment people remember. Our range covers indoor effects, low noise items and full aerial shells.</p>
        <p>Ask our team for advice on the right mix for your setting and local rules.</p></section>
      <section><h2>Great Service for Twenty Years</h2>
        <p>For two decades we have supplied dealers and display teams across Asia, Europe and beyond. Our partners return year after year for steady quality, fair pricing and fast, reliable shipping.</p></section>
    </div>
    <aside class="aside">
      <div class="quote">“The show was better than we hoped. Every guest was talking about it for weeks after.”<b>Tamsin Ferrow</b></div>
      <div class="promo"><b>Full Displays</b><br>Packages for every venue, from small gardens to city skylines.</div>
      <div class="brochure"><span class="ico"></span><div><small>Download our PDF catalogue or view our</small><strong>Virtual Brochure</strong></div></div>
    </aside>
  </div>
</section>

<section class="testimonials">
  <h2 class="section-title">TESTIMONIALS</h2>
  <blockquote>We have ordered from this team for many seasons and the quality never drops. Colours are rich, timing is tight and the paperwork is always in order. Their display crew handled our festival finale with real care, and the crowd loved every minute. We will be back again next year without a doubt.</blockquote>
  <div class="dots"><i class="on"></i><i></i><i></i></div>
</section>

<footer class="site-footer">
  <div class="wrap">
    <div class="links">
      <h4>LINKS</h4>
      <ul><li>Home</li><li>About</li><li>Shop</li><li>Gallery</li><li>Safety</li><li>Delivery</li><li>Blog</li><li>FAQs</li><li>Address</li><li>Privacy</li><li>Terms</li><li>Contact</li></ul>
      <div class="pay"><b>Secure Purchasing</b> – We accept the following methods of payment
        <div class="cards"><i></i><i></i><i></i><i></i><i></i></div></div>
    </div>
    <ul class="follow">
      <h4>FOLLOW US ON</h4>
      <li><i class="soc"></i>Friendwall</li>
      <li><i class="soc"></i>Chirpline</li>
      <li><i class="soc"></i>Reelcast</li>
      <li><i class="soc"></i>Pinboardly</li>
      <li><i class="soc"></i>Circlenet</li>
    </ul>
    <div class="offers">
      <h4>OFFERS AND SPECIALS</h4>
      <p>Enter your email below to receive our latest offers and specials.</p>
      <div class="field"></div>
      <a class="btn" href="#">SIGN UP</a>
    </div>
  </div>
</footer>
<div class="legal"><div class="wrap"><span>© 2014 brightpeonyhall.com.hk – All Rights Reserved</span><span>Site by Studio Orla</span></div></div>

</body>
</html>
```